Brake Test Training for Coal Mining

We offer Brake Test Training for Coal Mine workers. It's a legislative requirement that workers who are tasked with performing brake testing have certain competencies to do so. We test Light Vehicles and trailers, Heavy Vehicles and Mobile Mining Equipment like Graders, Scrapers and Dump Trucks.

```html
<!DOCTYPE html>
<html lang="en">
<head>
<meta charset="utf-8">
<title>Brake Test Training for Coal Mining</title>
<link rel="stylesheet" href="https://fonts.googleapis.com/css2?family=Bebas+Neue&family=Montserrat:wght@700&display=swap">
<style>
  :root {
    --page-bg: #d9d9d9;
    --paper: #f1f1f3;
    --navy: #1f2f6b;
    --navy-deep: #243a7c;
    --sky-blue: #3a80c0;
    --sun-yellow: #f4bd3d;
    --signal-orange: #e86f2d;
    --white: #ffffff;
    --photo-light: #d9ae45;
    --photo-mid: #9a7a38;
    --photo-dark: #4f4a3a;
  }
  html, body {
    margin: 0;
    width: 1200px;
    height: 1200px;
    overflow: hidden;
    background: var(--page-bg);
  }
  .billboard {
    position: absolute;
    left: 40px;
    top: 320px;
    width: 1120px;
    height: 560px;
    display: block;
  }
  .paper-band { fill: var(--paper); }
  .accent-stripe { fill: var(--signal-orange); }
  .phone-panel { fill: var(--sun-yellow); }
  .headline {
    font-family: "Bebas Neue", "Oswald", sans-serif;
    fill: var(--white);
  }
  .phone-number {
    font-family: "Bebas Neue", "Oswald", sans-serif;
    fill: var(--navy);
  }
  .phone-badge { fill: var(--navy); }
  .phone-glyph { fill: var(--sun-yellow); }
  .brand-dot { fill: var(--navy); }
  .brand-name {
    font-family: "Montserrat", sans-serif;
    font-weight: 700;
    fill: var(--navy);
  }
</style>
</head>
<body>
<svg class="billboard" viewBox="0 0 1239 620" preserveAspectRatio="none" xmlns="http://www.w3.org/2000/svg">
  <defs>
    <linearGradient id="hero-blue" x1="0" y1="0" x2="1" y2="0">
      <stop offset="0" stop-color="var(--navy-deep)"/>
      <stop offset="0.45" stop-color="#2b4f92"/>
      <stop offset="1" stop-color="var(--sky-blue)"/>
    </linearGradient>
    <linearGradient id="truck-tones" x1="0" y1="0" x2="0.4" y2="1">
      <stop offset="0" stop-color="var(--photo-light)"/>
      <stop offset="0.55" stop-color="var(--photo-mid)"/>
      <stop offset="1" stop-color="var(--photo-dark)"/>
    </linearGradient>
  </defs>

  <!-- background bands -->
  <rect class="paper-band" x="0" y="0" width="1239" height="216"/>
  <polygon class="phone-panel" points="716,0 1239,0 1239,218 668,216"/>
  <polygon class="accent-stripe" points="676,0 716,0 668,216 622,216"/>
  <rect x="0" y="216" width="1239" height="404" fill="url(#hero-blue)"/>

  <!-- brand -->
  <circle class="brand-dot" cx="112" cy="110" r="44"/>
  <text class="brand-name" x="180" y="112" font-size="38" textLength="280" lengthAdjust="spacingAndGlyphs">SUMMIT</text>
  <text class="brand-name" x="180" y="146" font-size="22" textLength="280" lengthAdjust="spacingAndGlyphs">OPERATOR TRAINING</text>

  <!-- phone -->
  <g class="phone-contact">
    <circle class="phone-badge" cx="850" cy="83" r="34"/>
    <path class="phone-glyph" d="M836 66c3-2 6-1 7 2l4 8c1 2 0 4-2 5l-3 2c2 5 6 9 11 12l2-3c1-2 3-3 5-2l8 4c3 1 4 4 2 7l-3 4c-2 3-6 4-10 3-13-4-23-14-27-27-1-4 0-8 3-10z"/>
    <text class="phone-number" x="906" y="110" font-size="74" textLength="292" lengthAdjust="spacingAndGlyphs">1300 555 019</text>
  </g>

  <!-- hero photo area -->
  <rect x="480" y="128" width="759" height="492" rx="6" fill="url(#truck-tones)" role="img" aria-label="Photo of a large yellow mining haul truck loaded with ore"/>

  <!-- headline -->
  <text class="headline" x="42" y="410" font-size="217" textLength="408" lengthAdjust="spacingAndGlyphs">BRAKE</text>
  <text class="headline" x="44" y="496" font-size="96" textLength="405" lengthAdjust="spacingAndGlyphs">TEST TRAINING</text>
  <text class="headline" x="42" y="578" font-size="86" textLength="407" lengthAdjust="spacingAndGlyphs">FOR COAL MINING</text>
</svg>
</body>
</html>
```